Business card Zottelgarten

Business card is for a self-employed dog trainer with own dog school. Name and logo of the dog school are available. Color specifications as well. The design should be classy and minimalist, but also modern. An already existing idea would be: Front: Only the logo Back: Contact data

Font styles to use
Serif
Sans Serif
Other font styles liked:
• Trajan Pro

Colors
f78f20

Requirements
Must have
• Name: Margit Wendler-Rasch Title: Dipl. Dog Trainer Contain my logo Follow my font and color preferences (see files)

```html
<!DOCTYPE html>
<html lang="de">
<head>
<meta charset="utf-8">
<title>Zottelgarten – Business Card</title>
<link rel="stylesheet" href="https://fonts.googleapis.com/css2?family=Cinzel:wght@400;500&family=Source+Sans+3:wght@300;400&display=swap">
<style>
  :root {
    --backdrop: #ababab;
    --brown: #6e5a4b;
    --cream: #f2efec;
    --card-light: #efefef;
    --ink: #6e5a4b;
    --faint: rgba(110, 90, 75, 0.06);
  }
  * { box-sizing: border-box; margin: 0; padding: 0; }
  html, body { width: 1200px; height: 576px; overflow: hidden; }
  body { background: var(--backdrop); position: relative; }

  .card {
    position: absolute;
    top: 138px;
    width: 484px;
    height: 294px;
    border-radius: 14px;
    overflow: hidden;
  }
  .card--front { left: 82px; background: var(--brown); }
  .card--back { left: 602px; background: var(--card-light); }

  .brand { position: absolute; text-align: center; }
  .brand__disc { border-radius: 50%; margin: 0 auto; }
  .brand__name {
    font-family: "Cinzel", serif;
    font-weight: 400;
    line-height: 1;
    white-space: nowrap;
  }
  .brand__url {
    font-family: "Cinzel", serif;
    line-height: 1;
    white-space: nowrap;
  }

  .card--front .brand { left: 0; width: 484px; top: 48px; }
  .card--front .brand__disc { width: 140px; height: 140px; background: var(--cream); }
  .card--front .brand__name { color: var(--cream); font-size: 28px; letter-spacing: 1px; margin-top: 12px; }
  .card--front .brand__url { color: var(--cream); font-size: 8.5px; letter-spacing: 3.4px; margin-top: 4px; }

  .card--back .brand { left: 28px; width: 180px; top: 67px; }
  .card--back .brand__disc { width: 118px; height: 118px; background: var(--brown); }
  .card--back .brand__name { color: var(--ink); font-size: 18px; letter-spacing: 0.6px; margin-top: 8px; }
  .card--back .brand__url { color: var(--ink); font-size: 6px; letter-spacing: 2.4px; margin-top: 3px; }

  .backdrop-disc {
    position: absolute;
    left: 278px; top: 38px;
    width: 250px; height: 250px;
    border-radius: 50%;
    background: var(--faint);
  }

  .person { position: absolute; left: 236px; top: 73px; color: var(--ink); }
  .person__name {
    font-family: "Cinzel", serif;
    font-size: 18px;
    letter-spacing: 0.4px;
    line-height: 1;
  }
  .person__title {
    font-family: "Source Sans 3", sans-serif;
    font-size: 9.5px;
    margin-top: 10px;
  }

  .contact { list-style: none; margin-top: 27px; }
  .contact__item {
    display: flex;
    align-items: center;
    height: 19px;
    font-family: "Source Sans 3", sans-serif;
    font-weight: 300;
    font-size: 13px;
    color: var(--ink);
  }
  .contact__icon { width: 11px; height: 11px; margin: 0 8px 0 6px; fill: var(--ink); }
</style>
</head>
<body>
  <section class="card card--front">
    <div class="brand">
      <div class="brand__disc"></div>
      <div class="brand__name">ZOTTELGARTEN</div>
      <div class="brand__url">WWW.ZOTTELGARTEN.CH</div>
    </div>
  </section>

  <section class="card card--back">
    <div class="backdrop-disc"></div>
    <div class="brand">
      <div class="brand__disc"></div>
      <div class="brand__name">ZOTTELGARTEN</div>
      <div class="brand__url">WWW.ZOTTELGARTEN.CH</div>
    </div>

    <div class="person">
      <div class="person__name">Margit Wendler-Rasch</div>
      <div class="person__title">Dipl. Dog Trainer</div>
      <ul class="contact">
        <li class="contact__item">
          <svg class="contact__icon" viewBox="0 0 12 12"><path d="M1 4.5C1 3 3 2 6 2s5 1 5 2.5v.8H8.6V4.2C7.8 4 6.9 3.9 6 3.9S4.2 4 3.4 4.2v1.1H1z"/><path d="M3.2 5.6h5.6L10.5 10h-9z"/></svg>
          (123) 456-7890
        </li>
        <li class="contact__item">
          <svg class="contact__icon" viewBox="0 0 12 12"><path d="M1 2.5h10v.6L6 6.4 1 3.1z"/><path d="M1 4.3l5 3.3 5-3.3V9.5H1z"/></svg>
          margit@zottelgarten.ch
        </li>
        <li class="contact__item">
          <svg class="contact__icon" viewBox="0 0 12 12"><path d="M6 1a5 5 0 1 0 0 10A5 5 0 0 0 6 1zm0 1.1c.5.6 1 1.6 1.2 2.9H4.8C5 3.7 5.5 2.7 6 2.1zM2.2 6.6h1.6c.1 1 .3 1.9.7 2.6a4 4 0 0 1-2.3-2.6zm0-1.2a4 4 0 0 1 2.3-2.6c-.4.7-.6 1.6-.7 2.6zM6 9.9c-.5-.6-1-1.6-1.2-3.3h2.4C7 8.3 6.5 9.3 6 9.9zm1.5-.7c.4-.7.6-1.6.7-2.6h1.6a4 4 0 0 1-2.3 2.6zm.7-3.8c-.1-1-.3-1.9-.7-2.6a4 4 0 0 1 2.3 2.6z"/></svg>
          www.zottelgarten.ch
        </li>
        <li class="contact__item">
          <svg class="contact__icon" viewBox="0 0 12 12"><path d="M6 .8a3.7 3.7 0 0 0-3.7 3.7C2.3 7.3 6 11.5 6 11.5s3.7-4.2 3.7-7A3.7 3.7 0 0 0 6 .8zm0 5.1a1.4 1.4 0 1 1 0-2.8 1.4 1.4 0 0 1 0 2.8z"/></svg>
          Lindenweg 12, Kloten
        </li>
      </ul>
    </div>
  </section>
</body>
</html>
```